Webpage layout and company logo combination

We are trying to renovate an existing site to make it sharper and sophisticated in appearance. This is the existing site: http://www.pellmoorrealtynj.com/agents.html . The new presentation should be bright, sharp, sophisticated and should incorporate two additional menu tabs. The menu tabs will be revised as follows: Property Listings, Property Management, Advisory & Consulting, Local Info, R/E Tools, Our Team (please disregard Korean language characters, which will be installed after English version is completed, separately).

It Company

```html
<!DOCTYPE html>
<html lang="en">
<head>
<meta charset="utf-8">
<title>Pellmoor Realty</title>
<link href="https://fonts.googleapis.com/css2?family=Oswald:wght@300;400;500&family=Arimo:wght@400&display=swap" rel="stylesheet">
<style>
:root{
  --orange:#f05a24;
  --dark-gray:#6b6b6b;
  --mid-gray:#9a9a9a;
  --light-gray:#ececec;
  --field-gray:#d9d9d9;
  --footer-bg:#d6d6d6;
  --footer-band:#7a7a7a;
  --text:#555;
  --white:#fff;
}
*{margin:0;padding:0;box-sizing:border-box}
html,body{width:706px;height:1200px;overflow:hidden;background:var(--white)}
body{position:relative;font-family:'Oswald',sans-serif;color:var(--text)}
.abs{position:absolute}

/* header */
.brand{left:50px;top:20px;display:flex;align-items:center;gap:8px}
.brand-mark{width:32px;height:30px;background:var(--orange)}
.brand-name{font-size:21px;font-weight:500;color:var(--orange);line-height:1}
.contact-line{right:50px;top:18px;font-size:14px;font-weight:300;color:var(--orange)}
.main-nav{left:262px;top:47px;display:flex;gap:10px;font-size:11.5px;color:#444;font-weight:400}
.main-nav a{color:inherit;text-decoration:none;position:relative;white-space:nowrap}
.main-nav a.active{color:#333}
.main-nav a.active::after{content:"";position:absolute;left:50%;bottom:-20px;transform:translateX(-50%);width:36px;height:5px;background:var(--orange)}

/* hero */
.hero{left:0;top:75px;width:706px;height:203px;background:linear-gradient(180deg,#2e3a55 0%,#5a6f95 35%,#c6a27a 60%,#3a2e28 100%)}
.hero-title{left:64px;top:124px;font-size:27px;font-weight:400;color:var(--white);line-height:36px;letter-spacing:-.3px}

/* search panel */
.search-panel{left:53px;top:215px;width:142px;height:486px;background:var(--white);border-radius:6px;box-shadow:0 2px 10px rgba(0,0,0,.25)}
.field{position:absolute;height:16px;border:1px solid #c9c9c9;border-radius:3px;background:#f5f5f5;font-family:'Arimo',sans-serif;font-size:6px;color:#777;padding-left:7px;line-height:14px}
.field.select::after{content:"";position:absolute;right:6px;top:4px;width:4px;height:4px;border-right:1.3px solid #666;border-bottom:1.3px solid #666;transform:rotate(45deg)}
.search-btn{position:absolute;left:105px;top:16px;width:22px;height:17px;background:var(--orange);border-radius:0 3px 3px 0}
.panel-heading{position:absolute;left:14px;font-size:11px;color:var(--orange);font-weight:400}
.small-label{position:absolute;font-size:6px;color:#666;font-family:'Arimo',sans-serif}
.btn{position:absolute;left:14px;width:114px;height:15px;font-family:'Arimo',sans-serif;font-size:5.5px;color:var(--white);text-align:center;line-height:15px;background:#c3c3c3}
.btn.primary{background:var(--orange)}
.section-label{position:absolute;left:14px;font-size:10px;color:#555}
.arrows{position:absolute;font-size:10px;color:#555;letter-spacing:1px}
.photo{position:absolute}

/* listings */
.listings-bar{left:218px;top:292px;width:436px;height:24px;background:var(--orange);color:var(--white);font-size:13px;padding-left:21px;line-height:24px}
.card{position:absolute;width:202px}
.card .photo{left:0;top:0;width:202px;height:144px}
.badge{position:absolute;left:0;top:10px;height:24px;padding:0 6px;background:var(--orange);color:var(--white);font-family:'Arimo',sans-serif;font-size:7.5px;line-height:24px}
.badge.muted{background:var(--dark-gray)}
.card-body{position:absolute;left:0;top:156px;height:62px;border-left:4px solid var(--orange);padding-left:10px;width:202px}
.card-title{font-size:12.5px;color:#555;line-height:14px;margin-top:2px}
.card-loc{font-size:9px;color:#999;font-weight:300;margin-top:1px}
.card-text{font-size:9px;font-weight:300;color:#777;line-height:14px;margin-top:5px}
.details{position:absolute;left:4px;top:229px;font-size:9.5px;color:#555;font-weight:300}
.price{position:absolute;right:0;top:227px;width:71px;height:17px;background:var(--dark-gray);color:var(--white);font-size:9.5px;text-align:center;line-height:17px}
.stats{position:absolute;left:0;top:254px;width:202px;height:21px;background:var(--light-gray);display:flex;align-items:center;font-family:'Arimo',sans-serif;font-size:5.5px;color:#666}
.stats span{flex:1;display:flex;align-items:center;justify-content:center;gap:3px;border-right:1px solid #aaa;height:11px}
.stats span:last-child{border-right:0}

/* agents */
.agents-bar{left:53px;top:720px;width:142px;height:18px;background:var(--orange);color:var(--white);font-size:7.5px;padding-left:13px;line-height:18px}
.agent{position:absolute;width:52px}
.agent .photo{left:0;top:0;width:52px;height:52px}
.agent-name{position:absolute;left:0;top:53px;border-left:2px solid var(--orange);padding-left:3px;font-family:'Arimo',sans-serif;font-size:5.5px;color:var(--orange);line-height:7px;width:60px;padding-top:3px;height:18px}

/* footer */
.footer-band{left:0;top:932px;width:706px;height:10px;background:var(--footer-band)}
.footer{left:0;top:942px;width:706px;height:258px;background:var(--footer-bg)}
.foot-heading{position:absolute;font-size:9px;color:#555;font-weight:400}
.contact-item{position:absolute;left:144px;display:flex;gap:4px;font-family:'Arimo',sans-serif;font-size:6px;color:#666;line-height:10px}
.contact-item svg{flex:none;margin-top:1px}
.foot-note{position:absolute;left:289px;top:47px;font-family:'Arimo',sans-serif;font-size:6px;color:#777}
.input{position:absolute;background:#c9c9c9;font-family:'Arimo',sans-serif;font-size:6px;color:#888;padding:5px 6px}
.send{position:absolute;left:493px;top:163px;width:71px;height:16px;background:#c0c0c0;font-size:9px;font-weight:300;color:#555;text-align:center;line-height:16px}
.footer-rule{position:absolute;left:110px;top:200px;width:490px;height:1px;background:linear-gradient(90deg,transparent,#999,transparent)}
.copyright{position:absolute;left:0;top:217px;width:706px;text-align:center;font-family:'Arimo',sans-serif;font-size:6.5px;color:#777}
</style>
</head>
<body>

<header>
  <div class="abs brand"><span class="brand-mark"></span><span class="brand-name">Pellmoor Realty</span></div>
  <div class="abs contact-line">Contact Us: (866)555-0142</div>
  <nav class="abs main-nav">
    <a class="active" href="#">Propery Listings</a>
    <a href="#">Property Managemtn</a>
    <a href="#">Advisory &amp; Consulting</a>
    <a href="#">Local Info</a>
    <a href="#">R/E Tools</a>
    <a href="#">Our Team</a>
  </nav>
</header>

<section class="abs hero" role="img" aria-label="Modern house lit at dusk with a hand holding out house keys"></section>
<h1 class="abs hero-title">Welcome Home<br>Open The Door To Your Dreams</h1>

<aside class="abs search-panel">
  <div class="field" style="left:14px;top:16px;width:92px;height:17px;line-height:15px">Search For Property</div>
  <div class="search-btn">
    <svg width="22" height="17" viewBox="0 0 22 17"><circle cx="10" cy="7.5" r="3" fill="none" stroke="#fff" stroke-width="1.3"/><line x1="12.2" y1="9.7" x2="14.5" y2="12" stroke="#fff" stroke-width="1.4"/></svg>
  </div>
  <div class="panel-heading" style="top:42px">FIND YOUR NEW HOME</div>
  <div class="field select" style="left:14px;top:67px;width:113px">LOCATION</div>
  <div class="field select" style="left:14px;top:91px;width:113px">RENT OR BUY</div>
  <div class="field select" style="left:14px;top:115px;width:113px">TYPE</div>
  <div class="field select" style="left:14px;top:140px;width:53px">BEDROOMS</div>
  <div class="field select" style="left:74px;top:140px;width:53px">BATHOOMS</div>
  <div class="panel-heading" style="top:165px;font-size:8px">PRICE</div>
  <div class="small-label" style="left:36px;top:181px">MIN</div>
  <div class="small-label" style="left:95px;top:181px">MAX</div>
  <div class="field" style="left:14px;top:189px;width:53px;height:14px;line-height:12px;text-align:center;padding:0;border-radius:4px;background:#fff">$ 100000</div>
  <div class="field" style="left:74px;top:189px;width:53px;height:14px;line-height:12px;text-align:center;padding:0;border-radius:4px;background:#fff">$ 900000</div>
  <div class="btn" style="top:215px">FIND PROPERTY</div>
  <div class="btn primary" style="top:240px">MORTGAGE CALCULATOR</div>
  <div class="btn" style="top:264px;background:#a9a9a9">FEATURED PROPERTIES</div>
  <div class="section-label" style="top:291px">FEATURED PROPERTIES</div>
  <div class="arrows" style="left:115px;top:291px">‹ ›</div>
  <div class="photo" style="left:14px;top:314px;width:114px;height:81px;background:linear-gradient(180deg,#7aa3c8 0%,#b9cede 45%,#4d5a3e 75%,#6e7a5a 100%)" role="img" aria-label="Glass pavilion house among trees"></div>
  <div style="position:absolute;left:14px;top:400px;border-left:2px solid var(--orange);padding-left:5px;height:26px;width:114px">
    <div style="font-size:7px;color:#555">Fort Lee</div>
    <div style="font-family:'Arimo',sans-serif;font-size:4.5px;color:#999">NJ, USA</div>
    <div style="font-family:'Arimo',sans-serif;font-size:4.5px;color:#888;line-height:6px;margin-top:2px">Pellentesque habitant morbi tristique senectus et netus et malesuada fames ac turpis egestas.</div>
  </div>
  <div style="position:absolute;left:16px;top:442px;font-size:6px;color:#555;font-weight:300">› Show Details</div>
  <div style="position:absolute;left:95px;top:441px;width:33px;height:10px;background:var(--dark-gray);color:#fff;font-size:5.5px;text-align:center;line-height:10px">$2.650.000</div>
  <div style="position:absolute;left:14px;top:457px;width:114px;height:11px;background:var(--light-gray);display:flex;font-family:'Arimo',sans-serif;font-size:3.5px;color:#777;align-items:center">
    <span style="flex:1;text-align:center;border-right:1px solid #bbb">⌂ 600 sqm</span>
    <span style="flex:1;text-align:center;border-right:1px solid #bbb">▬ 3</span>
    <span style="flex:1;text-align:center">▲ 2</span>
  </div>
</aside>

<section>
  <div class="abs agents-bar">OUR AGENTS<span style="position:absolute;right:12px;font-size:10px">‹ ›</span></div>
  <div class="agent" style="left:65px;top:748px">
    <div class="photo" style="background:linear-gradient(180deg,#7a3b2a,#3c2a28)" role="img" aria-label="Portrait of agent Henry Voss"></div>
    <div class="agent-name">HENRY VOSS</div>
  </div>
  <div class="agent" style="left:133px;top:748px">
    <div class="photo" style="background:linear-gradient(180deg,#e8ecef,#c9d6e2)" role="img" aria-label="Portrait of agent Milo Hartwell"></div>
    <div class="agent-name">MILO<br>HARTWELL</div>
  </div>
  <div class="agent" style="left:65px;top:829px">
    <div class="photo" style="background:linear-gradient(180deg,#f1f1f1,#e2d8cc)" role="img" aria-label="Portrait of agent Nora Fielding"></div>
    <div class="agent-name">NORA FIELDING</div>
  </div>
  <div class="agent" style="left:133px;top:829px">
    <div class="photo" style="background:linear-gradient(180deg,#ededed,#3a3f48)" role="img" aria-label="Portrait of agent Dario Lenz"></div>
    <div class="agent-name">DARIO<br>LENZ</div>
  </div>
</section>

<main>
  <h2 class="abs listings-bar" style="font-weight:400">Recent Listings</h2>

  <article class="card" style="left:218px;top:334px">
    <div class="photo" style="background:linear-gradient(180deg,#7fa7c9 0%,#c5d6e3 40%,#6b7060 70%,#cfcfc8 100%)" role="img" aria-label="Modern glass house with flat roof among trees"></div>
    <div class="badge">REDUCED</div>
    <div class="card-body"><div class="card-title">Fort Lee</div><div class="card-loc">NJ, USA</div><div class="card-text">Pellentesque habitant morbi tristique senectus et netus et malesuada fames ac turpis egestas.</div></div>
    <div class="details">› Show Details</div><div class="price">$2.650.000</div>
    <div class="stats"><span>⌂ 600 sqm</span><span>▬ 3</span><span>▲ 2</span></div>
  </article>

  <article class="card" style="left:453px;top:334px">
    <div class="photo" style="background:linear-gradient(180deg,#a9c4dd 0%,#d9e4ec 35%,#9b7a5a 60%,#d8d4cd 100%)" role="img" aria-label="Wood-clad cubic modern house with palm tree"></div>
    <div class="badge">FOR SALE</div>
    <div class="card-body"><div class="card-title">LITTLE FERRY</div><div class="card-loc">NJ, USA</div><div class="card-text">Pellentesque habitant morbi tristique senectus et netus et malesuada fames ac turpis egestas.</div></div>
    <div class="details">› Show Details</div><div class="price">$1.450.000</div>
    <div class="stats"><span>⌂ 600 sqm</span><span>▬ 3</span><span>▲ 2</span></div>
  </article>

  <article class="card" style="left:218px;top:631px">
    <div class="photo" style="background:linear-gradient(180deg,#8d98a6 0%,#4b4540 45%,#c98a45 65%,#3f4a33 100%)" role="img" aria-label="Gabled modern house with lit windows at dusk"></div>
    <div class="badge muted">PENDING</div>
    <div class="card-body"><div class="card-title">Guttenberg</div><div class="card-loc">NJ, USA</div><div class="card-text">Pellentesque habitant morbi tristique senectus et netus et malesuada fames ac turpis egestas.</div></div>
    <div class="details">› Show Details</div><div class="price">$1.800 /month</div>
    <div class="stats"><span>⌂ 600 sqm</span><span>▬ 3</span><span>▲ 2</span></div>
  </article>

  <article class="card" style="left:453px;top:631px">
    <div class="photo" style="background:linear-gradient(180deg,#9aa6b5 0%,#6d6a62 40%,#c9964f 65%,#4a3a2c 100%)" role="img" aria-label="Open modern house lit at evening among trees"></div>
    <div class="badge">FOR RENT</div>
    <div class="card-body"><div class="card-title">Edgewater</div><div class="card-loc">NJ, USA</div><div class="card-text">Pellentesque habitant morbi tristique senectus et netus et malesuada fames ac turpis egestas.</div></div>
    <div class="details">› Show Details</div><div class="price">$2.550 /month</div>
    <div class="stats"><span>⌂ 600 sqm</span><span>▬ 3</span><span>▲ 2</span></div>
  </article>
</main>

<div class="abs footer-band"></div>
<footer class="abs footer">
  <div class="foot-heading" style="left:144px;top:24px">GET IN CONTACT</div>
  <div class="contact-item" style="top:50px"><svg width="7" height="7" viewBox="0 0 10 10"><path d="M2 0.5 L4 3 L3 4.2 Q4.5 6 5.8 7 L7 6 L9.5 8 L8 9.5 Q3 9 0.5 2 Z" fill="#f05a24"/></svg>PHONE1: +1 212-555-0187</div>
  <div class="contact-item" style="top:62px"><svg width="7" height="7" viewBox="0 0 10 10"><path d="M2 0.5 L4 3 L3 4.2 Q4.5 6 5.8 7 L7 6 L9.5 8 L8 9.5 Q3 9 0.5 2 Z" fill="#f05a24"/></svg>PHONE1: +1 212-555-0187</div>
  <div class="contact-item" style="top:82px"><svg width="7" height="9" viewBox="0 0 10 13"><path d="M5 0 A4.5 4.5 0 0 1 9.5 4.5 C9.5 8 5 13 5 13 C5 13 0.5 8 0.5 4.5 A4.5 4.5 0 0 1 5 0 Z" fill="#f05a24"/><circle cx="5" cy="4.5" r="1.6" fill="#d6d6d6"/></svg><span>418 Birchwood Avenue, Suite<br>210 Fort Lee, NJ 07024</span></div>
  <div class="contact-item" style="top:112px"><svg width="9" height="7" viewBox="0 0 12 8"><rect width="12" height="8" fill="#f05a24"/><path d="M0 0 L6 5 L12 0" fill="none" stroke="#d6d6d6" stroke-width="1"/></svg>contact@pellmoor.example</div>

  <div class="foot-heading" style="left:289px;top:24px">QUICK CONTACT</div>
  <div class="foot-note">Posuere velit aliquet duis mollis, est non commodo luctus et normal.</div>
  <div class="input" style="left:289px;top:61px;width:130px;height:16px">Name *</div>
  <div class="input" style="left:434px;top:61px;width:130px;height:16px">Email *</div>
  <div class="input" style="left:289px;top:85px;width:130px;height:16px">Phone</div>
  <div class="input" style="left:434px;top:85px;width:130px;height:16px">Fax</div>
  <div class="input" style="left:289px;top:109px;width:275px;height:46px">Your message</div>
  <div class="send">Send Message</div>
  <div class="footer-rule"></div>
  <div class="copyright">© Copyright 2014 Pellmoor Realty, All Rights Reserved.</div>
</footer>

</body>
</html>
```